Personal Training Boot Camp Poster

We need a poster design for a 2 upcoming boot camps which are called
Iron Forge, and Peak Blitz. We would like to see designs that incorporate our logo. We want the poster to be very appealing to clients.

Dates: February 2 - March 19th

Iron Forge : Monday's and Wednesday's 8pm-9pm
Peak Blitz : Tuesday's and Thursdays 8pm-9pm

Training

```html
<!DOCTYPE html>
<html lang="en">
<head>
<meta charset="utf-8">
<title>Summit Core Boot Camp Poster</title>
<link rel="stylesheet" href="https://fonts.googleapis.com/css2?family=Russo+One&family=Roboto+Condensed:wght@400;700&display=swap">
<style>
  :root {
    --page: #e9e9e7;
    --white: #ffffff;
    --black: #0d0d0d;
    --band-gray: #8e8e8e;
    --band-gray-light: #a9a9a9;
    --orange: #f07a2c;
    --red: #d9342a;
    --logo-orange: #ee7a2a;
    --tag-gray: #9a9a9a;
    --text-dark: #111111;
  }
  * { margin: 0; padding: 0; box-sizing: border-box; }
  html, body {
    width: 1200px; height: 1148px; overflow: hidden;
    background: var(--page);
  }
  .poster {
    position: absolute; left: 210px; top: 24px;
    width: 780px; height: 1100px;
    overflow: hidden; background: var(--white);
  }
  .poster-art { position: absolute; inset: 0; }
  .brand {
    position: absolute; left: 0; top: 150px; width: 780px;
    display: flex; flex-direction: column; align-items: center;
  }
  .brand-name {
    display: flex; align-items: center; gap: 14px;
    font-family: "Russo One", sans-serif; font-size: 44px;
    letter-spacing: 3px; color: var(--logo-orange);
  }
  .brand-mark { width: 26px; height: 26px; background: var(--logo-orange); }
  .brand-rule { width: 430px; height: 2px; background: var(--tag-gray); margin: 10px 0 8px; }
  .brand-tagline {
    font-family: "Roboto Condensed", sans-serif; font-size: 16px;
    letter-spacing: 2.5px; color: var(--tag-gray); text-transform: uppercase;
  }
  .dates {
    position: absolute; left: 0; top: 322px; width: 780px; text-align: center;
    font-family: "Russo One", sans-serif; font-size: 30px; font-style: italic;
    color: var(--text-dark); letter-spacing: 1px;
  }
  .camp { position: absolute; color: var(--text-dark); }
  .camp-title {
    font-family: "Russo One", sans-serif; font-size: 70px; line-height: 0.92;
    font-style: italic; text-transform: uppercase; letter-spacing: 1px;
  }
  .camp-time {
    font-family: "Roboto Condensed", sans-serif; font-weight: 700;
    font-size: 15px; text-transform: uppercase; margin-top: 6px;
  }
  .camp-iron { left: 64px; top: 470px; }
  .camp-peak { left: 386px; top: 870px; }
</style>
</head>
<body>
  <main class="poster">
    <svg class="poster-art" width="780" height="1100" viewBox="0 0 780 1100" xmlns="http://www.w3.org/2000/svg">
      <defs>
        <linearGradient id="band-grad" x1="0" y1="0" x2="0" y2="1">
          <stop offset="0" stop-color="var(--band-gray-light)"/>
          <stop offset="1" stop-color="var(--band-gray)"/>
        </linearGradient>
        <linearGradient id="iron-grad" x1="0" y1="0" x2="1" y2="0">
          <stop offset="0" stop-color="var(--orange)"/>
          <stop offset="1" stop-color="var(--red)"/>
        </linearGradient>
        <linearGradient id="photo-light" x1="0" y1="0" x2="1" y2="1">
          <stop offset="0" stop-color="#d8d8d8"/>
          <stop offset="1" stop-color="#9c9c9c"/>
        </linearGradient>
        <linearGradient id="photo-dark" x1="0" y1="0" x2="1" y2="1">
          <stop offset="0" stop-color="#2a2a2a"/>
          <stop offset="1" stop-color="#6a6a6a"/>
        </linearGradient>
        <linearGradient id="shred-grad" x1="0" y1="0" x2="1" y2="0">
          <stop offset="0" stop-color="#8a8a8a"/>
          <stop offset="1" stop-color="#a4a4a4"/>
        </linearGradient>
      </defs>
      <polygon class="header-band" points="95,0 780,0 780,30 620,290 0,290 0,150" fill="var(--black)"/>
      <rect class="date-band" x="0" y="290" width="780" height="112" fill="url(#band-grad)"/>
      <rect x="0" y="402" width="780" height="400" fill="#cfcfcf"/>
      <g role="img" aria-label="Photo of a woman training with dumbbells">
        <polygon points="560,402 780,402 780,802 360,802" fill="url(#photo-light)"/>
      </g>
      <polygon class="iron-panel" points="0,402 600,402 400,802 0,802" fill="url(#iron-grad)"/>
      <rect x="0" y="802" width="780" height="298" fill="url(#shred-grad)"/>
      <g role="img" aria-label="Photo of a muscular man flexing">
        <polygon points="0,802 330,802 190,1100 0,1100" fill="url(#photo-dark)"/>
      </g>
      <polygon class="corner-wedge" points="780,870 780,1100 640,1100" fill="var(--black)"/>
    </svg>

    <header class="brand">
      <div class="brand-name"><span class="brand-mark"></span>SUMMIT CORE</div>
      <div class="brand-rule"></div>
      <div class="brand-tagline">Train Hard - Push Limits - Rise Higher</div>
    </header>

    <p class="dates">February 2 - March 19 TH</p>

    <section class="camp camp-iron">
      <h2 class="camp-title">Iron<br>Forge</h2>
      <p class="camp-time">Monday's and Wednesday's 8pm-9pm</p>
    </section>

    <section class="camp camp-peak">
      <h2 class="camp-title">Peak<br>Blitz</h2>
      <p class="camp-time">Tuesday's and Thursdays 8pm-9pm</p>
    </section>
  </main>
</body>
</html>
```